Mobile technology Business Card Design Project

We need a business card design for our company based in Sydeny Australia, that takes a company's desktop sites and creates a mobile site compatible to all mobile/smartphone devices. This allows greater ease of use and generally faster business conversion than customers using a desktop site.
Our company is called VelqCore but we refer to it as Velq Corestreams. If this could be represented somewhere on the business card that would be great.
Am open to suggestions regarding the colours but a high tech  theme would be good.
Happy bidding!

Target Market(s)
Business owner that has a website and is reasonably savvy regarding online/mobile marketing.
Industry/Entity Type
Business
Requirements
Must have
- Business card details:
Director Peter Langwade
Address: 5/41 Dunmore rd, Kelbrook. 2087
Email: tbc
Web: www.velqcore.com.au
The cards need to have two different names for the two directors.
Gregory Halvane & Peter Langwade (two separate business cards)

```html
<!DOCTYPE html>
<html lang="en">
<head>
<meta charset="utf-8">
<title>VelqCore Business Cards</title>
<link rel="stylesheet" href="https://fonts.googleapis.com/css2?family=Quicksand:wght@500;700&family=Roboto+Condensed:wght@400;700&display=swap">
<style>
  :root {
    --page: #eeeff1;
    --card: #ffffff;
    --ink: #1d1d1d;
    --muted: #555555;
    --brand-blue: #1d9bd7;
    --soft-blue: #a9dcf3;
    --brand-orange: #f0951e;
    --card-radius: 16px;
  }
  * { box-sizing: border-box; margin: 0; padding: 0; }
  html, body { width: 1200px; height: 850px; overflow: hidden; background: var(--page); }
  .sheet { position: relative; width: 1200px; height: 850px; }

  .card {
    position: absolute;
    width: 450px;
    height: 293px;
    background: var(--card);
    border-radius: var(--card-radius);
    overflow: hidden;
    box-shadow: 0 3px 10px rgba(0,0,0,0.22);
  }

  /* Front */
  .card-front { left: 375px; top: 80px; }
  .front-brand {
    position: absolute; left: 0; right: 0; top: 96px;
    display: flex; align-items: center; justify-content: center; gap: 14px;
  }
  .brand-dot { width: 30px; height: 30px; border-radius: 50%; background: var(--brand-blue); }
  .brand-name {
    font-family: "Quicksand", sans-serif; font-weight: 500;
    font-size: 46px; color: var(--ink); letter-spacing: 1px;
  }
  .tagline {
    position: absolute; left: 0; right: 0; top: 168px; text-align: center;
    font-family: "Quicksand", sans-serif; font-weight: 700;
    font-size: 17px; color: var(--brand-orange); letter-spacing: 0.5px;
  }

  /* Back */
  .card-back.peter { left: 135px; top: 450px; }
  .card-back.gregory { left: 615px; top: 450px; }
  .top-band { position: absolute; left: 0; right: 0; top: 0; height: 15px; background: var(--brand-orange); }
  .web-band {
    position: absolute; left: 0; right: 0; bottom: 0; height: 42px;
    background: var(--brand-blue); color: #fff;
    font-family: "Roboto Condensed", sans-serif; font-size: 17px;
    display: flex; align-items: center; justify-content: center;
  }
  .deco-disc { position: absolute; left: 0; top: 15px; }
  .contact {
    position: absolute; right: 26px; text-align: right;
    font-family: "Roboto Condensed", sans-serif; color: var(--ink);
  }
  .person { top: 32px; }
  .person-name { font-weight: 700; font-size: 22px; line-height: 1.1; }
  .person-role { font-size: 16px; color: var(--muted); }
  .address { top: 168px; font-size: 16px; line-height: 1.55; }
</style>
</head>
<body>
<main class="sheet">

  <section class="card card-front" aria-label="Card front">
    <div class="front-brand">
      <span class="brand-dot"></span>
      <span class="brand-name">VelqCore</span>
    </div>
    <p class="tagline">Sites Built for Every Screen</p>
  </section>

  <section class="card card-back peter" aria-label="Card back, Peter Langwade">
    <div class="top-band"></div>
    <svg class="deco-disc" width="260" height="236" viewBox="0 0 260 236" aria-hidden="true">
      <circle cx="120" cy="130" r="122" fill="var(--soft-blue)" opacity="0.45"/>
    </svg>
    <div class="contact person">
      <p class="person-name">Peter Langwade</p>
      <p class="person-role">Director</p>
    </div>
    <div class="contact address">
      <p>5/41 Dunmore rd,</p>
      <p>Kelbrook. 2087</p>
      <p>Email: tbc</p>
    </div>
    <div class="web-band">Web: www.velqcore.com.au</div>
  </section>

  <section class="card card-back gregory" aria-label="Card back, Gregory Halvane">
    <div class="top-band"></div>
    <svg class="deco-disc" width="260" height="236" viewBox="0 0 260 236" aria-hidden="true">
      <circle cx="120" cy="130" r="122" fill="var(--soft-blue)" opacity="0.45"/>
    </svg>
    <div class="contact person">
      <p class="person-name">Gregory Halvane</p>
      <p class="person-role">Director</p>
    </div>
    <div class="contact address">
      <p>5/41 Dunmore rd,</p>
      <p>Kelbrook. 2087</p>
      <p>Email: tbc</p>
    </div>
    <div class="web-band">Web: www.velqcore.com.au</div>
  </section>

</main>
</body>
</html>
```